TillNimbus Flyer

Create a flyer that is smart / business looking to advertise our Point Of Sale Software.

Further info can be obtained from www.tillnimbus.com.au

Other info:
www.tillnimbus.com.au
admin@tillnimbus.com.au
PH: 1300 674 219

Target Market(s)

Business Owners , point of sale for business

Industry/Entity Type

Business

Colors

Designer to choose colors to be used in the design.

Requirements
Nice to have
• Perfer Company Colours
• www.tillnimbus.com.au
• but more important to look good
• More information can be found on our website

```html
<!DOCTYPE html>
<html lang="en">
<head>
<meta charset="utf-8">
<title>TillNimbus Flyer</title>
<link href="https://fonts.googleapis.com/css2?family=Montserrat:wght@300;400;500;700;800&display=swap" rel="stylesheet">
<style>
  :root {
    --red: #e01b24;
    --ink: #1c1c1c;
    --grey: #555;
    --paper: #ffffff;
    --paper-soft: #f4f4f5;
    --orange: #e0901c;
    --orange-dark: #b9650d;
    --footer: #1f1f20;
  }
  * { box-sizing: border-box; margin: 0; padding: 0; }
  html, body { width: 950px; height: 1200px; overflow: hidden; background: var(--paper); }
  body { font-family: "Montserrat", Arial, sans-serif; color: var(--ink); }
  .flyer { position: relative; width: 950px; height: 1200px; background: linear-gradient(180deg, #fff 0%, var(--paper-soft) 100%); overflow: hidden; }
  .art { position: absolute; inset: 0; width: 950px; height: 1200px; }

  .brand { position: absolute; left: 58px; top: 60px; }
  .brand-row { display: flex; align-items: center; gap: 12px; }
  .brand-dot { width: 34px; height: 34px; border-radius: 50%; background: var(--red); }
  .brand-name { font-size: 44px; font-weight: 700; color: var(--ink); letter-spacing: -1px; line-height: 1; }
  .brand-sub { margin-left: 240px; margin-top: 2px; font-size: 10px; color: var(--grey); }

  .intro { position: absolute; left: 60px; top: 402px; width: 414px; }
  .intro h1 { font-size: 45px; line-height: 49px; font-weight: 300; color: var(--ink); letter-spacing: -0.5px; }
  .intro h1 strong { font-weight: 800; color: var(--red); }
  .intro .rule { width: 96px; height: 4px; background: var(--red); margin: 6px 0 18px; }
  .intro p { font-size: 12.2px; line-height: 17.3px; color: var(--ink); margin-bottom: 10px; text-align: justify; }

  .pitch { position: absolute; top: 896px; left: 0; width: 950px; text-align: center; }
  .pitch h2 { font-size: 29px; line-height: 36px; font-weight: 800; color: var(--red); }
  .pitch p { font-size: 19px; line-height: 24px; font-weight: 400; }
  .pitch .rule { width: 100px; height: 3px; background: var(--red); margin: 12px auto 0; }

  .features { position: absolute; top: 992px; left: 88px; display: flex; }
  .features ul { list-style: none; }
  .features li { display: flex; align-items: center; gap: 7px; font-size: 14.5px; font-weight: 500; height: 22.5px; }
  .features .col-1 { width: 240px; }
  .features .col-2 { width: 178px; }
  .features .col-3 { width: 140px; }
  .tick { width: 12px; height: 12px; flex: none; }

  .footer { position: absolute; left: 0; bottom: 0; width: 950px; height: 62px; background: var(--footer); border-top: 3px solid var(--red); display: flex; justify-content: center; align-items: center; gap: 22px; color: #fff; font-size: 19.5px; }
  .contact { display: flex; align-items: center; gap: 10px; }
  .contact-icon { width: 22px; height: 22px; border-radius: 50%; background: var(--red); display: flex; align-items: center; justify-content: center; }
  .contact-icon svg { width: 12px; height: 12px; }
</style>
</head>
<body>
<div class="flyer">
  <svg class="art" viewBox="0 0 950 1200">
    <defs>
      <radialGradient id="techGlow" cx="0.62" cy="0.5" r="0.65">
        <stop offset="0" stop-color="#dff3ff"/>
        <stop offset="0.3" stop-color="#5fa8d6"/>
        <stop offset="0.7" stop-color="#17355f"/>
        <stop offset="1" stop-color="#08142a"/>
      </radialGradient>
    </defs>
    <polygon role="img" aria-label="Photo of a hand using a laptop surrounded by glowing network and email icons over a world map"
      points="469,0 950,0 950,721 406,880 330,300 420,200" fill="url(#techGlow)"/>
    <g class="shards" fill="var(--orange)">
      <polygon points="469,144 590,0 770,0 650,55 520,120"/>
      <polygon points="85,318 140,270 240,230 335,170 420,180 320,250 200,300"/>
      <polygon points="600,855 700,800 800,770 870,720 900,790 820,820 700,850"/>
      <polygon points="880,800 920,770 935,790" fill="var(--orange-dark)"/>
      <polygon points="760,850 800,830 790,860" fill="var(--orange-dark)"/>
      <polygon points="60,262 90,245 72,278" fill="var(--orange-dark)"/>
      <polygon points="160,214 192,203 172,228" fill="var(--orange-dark)"/>
      <polygon points="290,160 320,150 305,178" fill="var(--orange-dark)"/>
      <polygon points="650,12 680,18 660,40" fill="var(--red)"/>
    </g>
    <polygon class="hex" points="255,284 556,419 556,730 252,890 -10,750 -10,380" fill="#fff"/>
    <polygon class="hex-dash" points="255,300 540,430 540,720 252,872 8,752 8,390" fill="none" stroke="var(--red)" stroke-width="1.2" stroke-dasharray="4 3"/>
    <polygon points="0,770 75,805 75,880 0,915" fill="none" stroke="var(--red)" stroke-width="1" stroke-dasharray="4 3"/>
    <polygon points="130,812 160,797 190,812 190,846 160,861 130,846" fill="none" stroke="#bbb" stroke-width="1" stroke-dasharray="4 3"/>
    <polygon points="85,876 110,863 135,876 135,905 110,918 85,905" fill="#f4c5c8"/>
  </svg>

  <header class="brand">
    <div class="brand-row">
      <span class="brand-dot"></span>
      <span class="brand-name">TillNimbus</span>
    </div>
    <div class="brand-sub">powered by Korvex</div>
  </header>

  <section class="intro">
    <h1>LOREM IPSUM<br>IS <strong>SIMPLY<br>DUMMY TEXT</strong></h1>
    <div class="rule"></div>
    <p>Lorem Ipsum is simply dummy text of the printing and type&shy;setting industry. Lorem Ipsum has been the industry's stan&shy;dard dummy text ever since the 1500s, when an unknown printer took a galley of type and scrambled it to make a type specimen book.</p>
    <p>Lorem Ipsum is simply dummy text of the printing and type&shy;setting industry. Lorem Ipsum has been the industry's stan&shy;dard dummy text ever since the 1500s, when an unknown printer took a galley of type and scrambled it to make a type specimen book.</p>
  </section>

  <section class="pitch">
    <h2>All in One Point Of Sale System</h2>
    <p>That Records All Your Company Data in The One Package</p>
    <div class="rule"></div>
  </section>

  <section class="features">
    <ul class="col-1">
      <li><svg class="tick" viewBox="0 0 12 12"><rect x="1" y="2" width="9" height="9" fill="none" stroke="#e01b24" stroke-width="1.4"/><path d="M3 6l2.5 2.5L11 2" fill="none" stroke="#e01b24" stroke-width="1.6"/></svg>User friendly Point of Sale</li>
      <li><svg class="tick" viewBox="0 0 12 12"><rect x="1" y="2" width="9" height="9" fill="none" stroke="#e01b24" stroke-width="1.4"/><path d="M3 6l2.5 2.5L11 2" fill="none" stroke="#e01b24" stroke-width="1.6"/></svg>Management Dashboard</li>
      <li><svg class="tick" viewBox="0 0 12 12"><rect x="1" y="2" width="9" height="9" fill="none" stroke="#e01b24" stroke-width="1.4"/><path d="M3 6l2.5 2.5L11 2" fill="none" stroke="#e01b24" stroke-width="1.6"/></svg>Invoicing</li>
      <li><svg class="tick" viewBox="0 0 12 12"><rect x="1" y="2" width="9" height="9" fill="none" stroke="#e01b24" stroke-width="1.4"/><path d="M3 6l2.5 2.5L11 2" fill="none" stroke="#e01b24" stroke-width="1.6"/></svg>Statements</li>
      <li><svg class="tick" viewBox="0 0 12 12"><rect x="1" y="2" width="9" height="9" fill="none" stroke="#e01b24" stroke-width="1.4"/><path d="M3 6l2.5 2.5L11 2" fill="none" stroke="#e01b24" stroke-width="1.6"/></svg>Payments</li>
      <li><svg class="tick" viewBox="0 0 12 12"><rect x="1" y="2" width="9" height="9" fill="none" stroke="#e01b24" stroke-width="1.4"/><path d="M3 6l2.5 2.5L11 2" fill="none" stroke="#e01b24" stroke-width="1.6"/></svg>Products</li>
    </ul>
    <ul class="col-2">
      <li><svg class="tick" viewBox="0 0 12 12"><rect x="1" y="2" width="9" height="9" fill="none" stroke="#e01b24" stroke-width="1.4"/><path d="M3 6l2.5 2.5L11 2" fill="none" stroke="#e01b24" stroke-width="1.6"/></svg>Quotations</li>
      <li><svg class="tick" viewBox="0 0 12 12"><rect x="1" y="2" width="9" height="9" fill="none" stroke="#e01b24" stroke-width="1.4"/><path d="M3 6l2.5 2.5L11 2" fill="none" stroke="#e01b24" stroke-width="1.6"/></svg>Purchase Orders</li>
      <li><svg class="tick" viewBox="0 0 12 12"><rect x="1" y="2" width="9" height="9" fill="none" stroke="#e01b24" stroke-width="1.4"/><path d="M3 6l2.5 2.5L11 2" fill="none" stroke="#e01b24" stroke-width="1.6"/></svg>Expenses</li>
      <li><svg class="tick" viewBox="0 0 12 12"><rect x="1" y="2" width="9" height="9" fill="none" stroke="#e01b24" stroke-width="1.4"/><path d="M3 6l2.5 2.5L11 2" fill="none" stroke="#e01b24" stroke-width="1.6"/></svg>Gift Vouchers</li>
      <li><svg class="tick" viewBox="0 0 12 12"><rect x="1" y="2" width="9" height="9" fill="none" stroke="#e01b24" stroke-width="1.4"/><path d="M3 6l2.5 2.5L11 2" fill="none" stroke="#e01b24" stroke-width="1.6"/></svg>Warehousing</li>
      <li><svg class="tick" viewBox="0 0 12 12"><rect x="1" y="2" width="9" height="9" fill="none" stroke="#e01b24" stroke-width="1.4"/><path d="M3 6l2.5 2.5L11 2" fill="none" stroke="#e01b24" stroke-width="1.6"/></svg>Inventory</li>
    </ul>
    <ul class="col-3">
      <li><svg class="tick" viewBox="0 0 12 12"><rect x="1" y="2" width="9" height="9" fill="none" stroke="#e01b24" stroke-width="1.4"/><path d="M3 6l2.5 2.5L11 2" fill="none" stroke="#e01b24" stroke-width="1.6"/></svg>Laybys</li>
      <li><svg class="tick" viewBox="0 0 12 12"><rect x="1" y="2" width="9" height="9" fill="none" stroke="#e01b24" stroke-width="1.4"/><path d="M3 6l2.5 2.5L11 2" fill="none" stroke="#e01b24" stroke-width="1.6"/></svg>Barcodes</li>
      <li><svg class="tick" viewBox="0 0 12 12"><rect x="1" y="2" width="9" height="9" fill="none" stroke="#e01b24" stroke-width="1.4"/><path d="M3 6l2.5 2.5L11 2" fill="none" stroke="#e01b24" stroke-width="1.6"/></svg>Stocktake</li>
      <li><svg class="tick" viewBox="0 0 12 12"><rect x="1" y="2" width="9" height="9" fill="none" stroke="#e01b24" stroke-width="1.4"/><path d="M3 6l2.5 2.5L11 2" fill="none" stroke="#e01b24" stroke-width="1.6"/></svg>Users</li>
      <li><svg class="tick" viewBox="0 0 12 12"><rect x="1" y="2" width="9" height="9" fill="none" stroke="#e01b24" stroke-width="1.4"/><path d="M3 6l2.5 2.5L11 2" fill="none" stroke="#e01b24" stroke-width="1.6"/></svg>Customers</li>
      <li><svg class="tick" viewBox="0 0 12 12"><rect x="1" y="2" width="9" height="9" fill="none" stroke="#e01b24" stroke-width="1.4"/><path d="M3 6l2.5 2.5L11 2" fill="none" stroke="#e01b24" stroke-width="1.6"/></svg>Suppliers</li>
    </ul>
    <ul class="col-4">
      <li><svg class="tick" viewBox="0 0 12 12"><rect x="1" y="2" width="9" height="9" fill="none" stroke="#e01b24" stroke-width="1.4"/><path d="M3 6l2.5 2.5L11 2" fill="none" stroke="#e01b24" stroke-width="1.6"/></svg>GST</li>
      <li><svg class="tick" viewBox="0 0 12 12"><rect x="1" y="2" width="9" height="9" fill="none" stroke="#e01b24" stroke-width="1.4"/><path d="M3 6l2.5 2.5L11 2" fill="none" stroke="#e01b24" stroke-width="1.6"/></svg>Barcode Printing</li>
      <li><svg class="tick" viewBox="0 0 12 12"><rect x="1" y="2" width="9" height="9" fill="none" stroke="#e01b24" stroke-width="1.4"/><path d="M3 6l2.5 2.5L11 2" fill="none" stroke="#e01b24" stroke-width="1.6"/></svg>Multi-store Options</li>
      <li><svg class="tick" viewBox="0 0 12 12"><rect x="1" y="2" width="9" height="9" fill="none" stroke="#e01b24" stroke-width="1.4"/><path d="M3 6l2.5 2.5L11 2" fill="none" stroke="#e01b24" stroke-width="1.6"/></svg>Multi-Warehouse Options</li>
    </ul>
  </section>

  <footer class="footer">
    <div class="contact">
      <span class="contact-icon"><svg viewBox="0 0 12 12"><rect x="1" y="2" width="10" height="7" rx="1" fill="none" stroke="#fff" stroke-width="1.4"/><path d="M4 11h4" stroke="#fff" stroke-width="1.4"/></svg></span>
      <span>www.tillnimbus.com.au</span>
    </div>
    <div class="contact">
      <span class="contact-icon"><svg viewBox="0 0 12 12"><rect x="1" y="3" width="10" height="7" fill="#fff"/><path d="M1 3l5 4 5-4" fill="none" stroke="#e01b24" stroke-width="1.2"/></svg></span>
      <span>admin@tillnimbus.com.au</span>
    </div>
    <div class="contact">
      <span class="contact-icon"><svg viewBox="0 0 12 12"><path d="M2.5 1.5l2 0 1 2.5-1.3 1a6 6 0 0 0 2.8 2.8l1-1.3 2.5 1v2c0 .6-.5 1-1 1C5 10.3 1.7 7 1.5 2.5c0-.6.4-1 1-1z" fill="#fff"/></svg></span>
      <span>1300 674 219</span>
    </div>
  </footer>
</div>
</body>
</html>
```